Baby Cloth Business Needs a Web Design

We need a web design for a new company that produces and sells baby sleeping bags. We use brixVendor (demo.brixvendor.net) e-commerce software which we need a new design for that represents our products better. We would like to see designs that use simple and clean elements, playful layout with big pictures and emphasis on typography. We already have a logo that is "fresh" apple green so we would like colors that go well with that.
We use the following pages/features:
- Home page (with newsletter, chatterly link and contact us link)
- Category page (no search needed)
- Product details page (with share)
- User pages (register, login, my account)
- Shopping cart with all its pages (about 6-7)
- Static pages (3 pages: contact us, about us, conditions of use).

We need designs in the form of PSD

Target Market(s)

Primary: mothers 25-45; secondary: women 20-60 who buy it as gift

Industry/Entity Type

Business

Requirements
Must have
• Since the site uses brixVendor no other data can be added beside those already exist on site.
Nice to have
• We have photos taken for this site (sample attached) and would be nice to show them in big sizes. We would like to see imaginative, playful elements that appear several places throughout the site. Logo contains a small baby foot which could leave footprints here and there.

We like these sites (and what):
- http://www.plovik.net/13-organic-bamboo-cotton-baby-essentials (simple, nice but too gray)
- http://www.trelmark.net/ (logo placement, menu, background)
- http://www.zorpeli.net/
- http://www.qeb.net/website-template/view/html/baby-clothes?originUrl=http%3A%2F%2Fwww.qeb.net%2Fwebsite%2Ftemplates%2Fhtml%2Fonline-shop%2F2&galleryDocIndex=0 (layout, image sizes)
- http://themes.fashion.brix-layouts.net/?isOpen=false&;t_r=true (layout)
Should not have
• We do not use forum, blog, new products, manufacturers, popular tags, polls, search from brixVendor.

```html
<!DOCTYPE html>
<html lang="en">
<head>
<meta charset="utf-8">
<title>Snugbag – Smart sleeping bags for babies and kids</title>
<link rel="stylesheet" href="https://fonts.googleapis.com/css2?family=Open+Sans:wght@400;600;700&family=Handlee&family=Oswald:wght@500&display=swap">
<style>
:root{
  --green:#7ab648;
  --green-dark:#4f9a1c;
  --green-light:#8dcc25;
  --yellow:#f2f200;
  --ink:#333;
  --muted:#666;
  --line:#dcdcdc;
  --btn-dark:#555;
  --white:#fff;
}
*{box-sizing:border-box;margin:0;padding:0}
html,body{width:1131px;height:1200px;overflow:hidden;background:var(--white)}
body{font-family:"Open Sans",Arial,sans-serif;color:var(--ink)}
.page{position:absolute;left:0;top:0;width:1200px;height:1273px;transform:scale(.9425);transform-origin:0 0}
.abs{position:absolute}
.script{font-family:"Handlee",cursive;letter-spacing:1px}

/* top bar */
.topbar{left:0;top:0;width:1200px;height:42px;background:var(--green);color:var(--white);font-size:13px}
.topbar span,.topbar svg{position:absolute;top:13px}
.topbar svg{top:12px}

/* header */
.brand{left:130px;top:82px;font-size:42px;line-height:50px;color:var(--green);font-weight:400}
.tagline{left:170px;top:141px;font-size:8px;color:var(--green)}
.search{left:813px;top:55px;width:258px;height:24px;background:#f0f0f0;border-radius:3px;font-size:10px;color:#bbb;padding:5px 4px}
.search svg{position:absolute;right:10px;top:3px}
.nav{top:115px;font-size:19px;color:var(--ink)}
.nav-sep{top:116px;width:1px;height:17px;background:#333}

/* hero */
.hero{left:120px;top:168px;width:961px;height:344px;background:linear-gradient(90deg,#b98a5f 0%,#c9a27c 25%,#7fc9d8 30%,#8fcfdc 40%,#c5bcb2 58%,#d6d3cf 75%,#cfccc7 100%)}
.hero-title{left:693px;top:268px;font-size:30px;color:var(--white)}
.hero-text{left:692px;top:317px;width:350px;font-size:12.5px;line-height:24px;color:var(--white)}
.btn{display:flex;align-items:center;justify-content:center;color:var(--white);font-weight:600}
.btn-read{left:693px;top:420px;width:135px;height:40px;background:var(--green);font-size:16px}
.btn-buy{left:851px;top:420px;width:135px;height:40px;background:var(--btn-dark);font-size:16px}
.dots{left:954px;top:483px;display:flex;gap:2px}
.dots i{display:block;width:14px;height:14px;border-radius:50%;background:#333;border:2px solid #fff}
.dots i:first-child{background:#fff;border-color:#333}

/* products */
.section-title{font-size:23px;color:#444}
.card{top:590px;width:221px;height:141px;border:1px solid var(--line)}
.card-img{position:absolute;top:10px;left:70px;width:80px;height:120px;border-radius:30px 30px 22px 22px}
.sale-tag{position:absolute;left:8px;top:14px;width:42px;height:30px;background:var(--green);transform:rotate(-35deg);color:#fff;font-size:12px;display:flex;align-items:center;justify-content:center}
.sale-box{position:absolute;left:14px;top:72px;width:38px;height:38px;background:var(--green);color:#fff;font-size:11px;line-height:14px;font-weight:600;display:flex;flex-direction:column;align-items:center;justify-content:center}
.p-title{top:740px;font-size:12.5px;font-weight:600;color:var(--green)}
.p-desc{top:759px;width:200px;font-size:12.5px;line-height:20px;color:var(--muted)}
.p-price{top:797px;font-size:20px;font-weight:600}
.btn-cart{top:833px;width:104px;height:34px;background:var(--green-dark);font-size:13px}
.btn-info{top:833px;width:104px;height:34px;background:var(--green-light);font-size:13px}

/* lower boxes */
.box{top:947px;width:267px;height:170px;background:#fff;box-shadow:0 3px 8px rgba(0,0,0,.2)}
.social-brand{position:absolute;left:30px;top:10px;font-size:11px;color:var(--green)}
.like{position:absolute;left:175px;top:12px;font-size:9px}
.like b{display:inline-block;border:1px solid #aab;background:#eef;padding:1px 4px;font-weight:400;margin-right:4px}
.fans{position:absolute;left:27px;top:36px;display:grid;grid-template-columns:repeat(5,40px);column-gap:4px;row-gap:6px}
.fan{text-align:center;font-size:7px;color:#666}
.fan div{width:40px;height:40px;background:linear-gradient(#9aa4ad,#6c747b);margin-bottom:2px}
.plugin{position:absolute;left:27px;top:150px;width:218px;border-top:1px solid #ddd;padding-top:4px;font-size:8px;color:#3b5998;display:flex;gap:4px;align-items:center}
.plugin i{width:9px;height:9px;background:#3b5998;display:block}
.nl-head{position:absolute;left:18px;top:18px;display:flex;gap:10px;align-items:center;font-family:"Oswald",sans-serif;font-size:19px;color:var(--green)}
.nl-text{position:absolute;left:21px;top:50px;width:232px;font-size:9px;line-height:16px;color:#bbb}
.nl-input{position:absolute;left:24px;top:89px;width:225px;height:34px;background:#eee;border-top:2px solid #ccc;font-size:12px;color:#aaa;padding:8px 8px}
.nl-submit{position:absolute;left:169px;top:133px;width:82px;height:24px;background:var(--yellow);font-size:9px;font-weight:600;display:flex;align-items:center;justify-content:center}
.offer{left:786px;top:947px;width:267px;height:170px;background:linear-gradient(100deg,#cfd4d0,#e8e4dd 50%,#d6cfc4);overflow:hidden;box-shadow:0 3px 8px rgba(0,0,0,.2)}
.offer-circle{position:absolute;left:-40px;top:42px;width:142px;height:142px;border-radius:50%;background:var(--green);color:#fff;font-family:"Oswald",sans-serif;padding:26px 0 0 50px;line-height:1}
.offer-circle .a{font-size:25px}
.offer-circle .b{font-size:15px;color:var(--yellow);margin-top:3px}
.offer-circle .c{font-size:38px;margin-top:3px}

/* footer */
.footer{left:0;top:1178px;width:1200px;height:95px;background:var(--green);color:#fff;font-size:12.5px}
.foot-links{position:absolute;left:129px;top:22px;white-space:nowrap}
.foot-links span{margin:0 9px}
.copy{position:absolute;left:131px;top:54px}
.socials{position:absolute;left:918px;top:30px;display:flex;gap:8px}
.socials i{display:block;width:32px;height:32px;border-radius:50%;background:#fff}
</style>
</head>
<body>
<div class="page">

  <div class="abs topbar">
    <span style="left:550px">Welcome&nbsp;&nbsp;:</span>
    <svg style="left:625px" width="18" height="17" viewBox="0 0 18 17"><path d="M2 6h14l-2 10H4z M5 6l4-5 4 5" fill="none" stroke="#fff" stroke-width="1.6"/></svg>
    <span style="left:652px">Shopping Bag: (empty)</span>
    <svg style="left:803px" width="14" height="16" viewBox="0 0 14 16"><circle cx="7" cy="4.5" r="4" fill="#fff"/><path d="M0 16c0-5 3-7 7-7s7 2 7 7z" fill="#fff"/></svg>
    <span style="left:825px">Your Account</span>
    <span style="left:916px">|</span>
    <svg style="left:928px" width="12" height="16" viewBox="0 0 12 16"><path d="M3 7V4a3 3 0 0 1 6 0v3" fill="none" stroke="#fff" stroke-width="2"/><rect x="0" y="7" width="12" height="9" fill="#fff"/></svg>
    <span style="left:946px">Login</span>
    <svg style="left:991px;top:14px" width="27" height="15" viewBox="0 0 27 15"><rect width="27" height="15" fill="#2a3f8f"/><path d="M0 0L27 15M27 0L0 15" stroke="#fff" stroke-width="3"/><path d="M13.5 0v15M0 7.5h27" stroke="#fff" stroke-width="5"/><path d="M13.5 0v15M0 7.5h27" stroke="#c8102e" stroke-width="3"/></svg>
    <span style="left:1025px">English</span>
    <svg style="left:1071px;top:18px" width="9" height="7" viewBox="0 0 9 7"><path d="M0 0h9L4.5 7z" fill="#4c7a2c"/></svg>
  </div>

  <div class="abs brand">Snugbag</div>
  <div class="abs tagline">smart sleeping bag for babies and kids</div>

  <div class="abs search">Search
    <svg width="20" height="19" viewBox="0 0 20 19"><circle cx="8" cy="8" r="6" fill="none" stroke="#999" stroke-width="2"/><path d="M12.5 12.5l6 5.5" stroke="#999" stroke-width="2.5"/></svg>
  </div>

  <nav>
    <span class="abs nav script" style="left:444px">Home</span>
    <i class="abs nav-sep" style="left:508px"></i>
    <span class="abs nav script" style="left:537px">About Us</span>
    <i class="abs nav-sep" style="left:640px"></i>
    <span class="abs nav script" style="left:664px">Sleeping Bags</span>
    <i class="abs nav-sep" style="left:792px"></i>
    <span class="abs nav script" style="left:815px">Gifts</span>
    <i class="abs nav-sep" style="left:880px"></i>
    <span class="abs nav script" style="left:910px">Sale</span>
    <i class="abs nav-sep" style="left:960px"></i>
    <span class="abs nav script" style="left:983px">Contact Us</span>
  </nav>

  <div class="abs hero" role="img" aria-label="Photo of a smiling toddler in a blue polka-dot sleeping bag"></div>
  <div class="abs hero-title script">Baby Sleeping Bags</div>
  <p class="abs hero-text">ed ut perspiciatis unde omnis iste natus error sit voluptatem accusantium doloremque laudantium, totam rem aperiam, eaque ipsa quae ab illo inventore veritatis et quasi architecto beatae vitae dicta sunt explicabo.</p>
  <div class="abs btn btn-read">Read More</div>
  <div class="abs btn btn-buy">Buy Now</div>
  <div class="abs dots"><i></i><i></i><i></i><i></i></div>

  <h2 class="abs section-title script" style="left:538px;top:538px">Our Products</h2>
  <svg class="abs" style="left:133px;top:555px" width="20" height="28" viewBox="0 0 20 28"><path d="M17 2L4 14l13 12" fill="none" stroke="#999" stroke-width="2.5"/></svg>
  <svg class="abs" style="left:1050px;top:555px" width="20" height="28" viewBox="0 0 20 28"><path d="M3 2l13 12L3 26" fill="none" stroke="#999" stroke-width="2.5"/></svg>

  <div class="abs card" style="left:129px">
    <div class="card-img" role="img" aria-label="White sleeping bag with pink trim" style="background:linear-gradient(#f6e6ef,#fafafa)"></div>
    <div class="sale-tag">SALE</div><div class="sale-box"><span>25%</span><span>Sale</span></div>
  </div>
  <div class="abs card" style="left:369px">
    <div class="card-img" role="img" aria-label="Cream teddy-bear sleeping bag" style="background:linear-gradient(#e7d3b0,#f1e6d2)"></div>
  </div>
  <div class="abs card" style="left:609px">
    <div class="card-img" role="img" aria-label="Light blue sleeping bag" style="background:linear-gradient(#9fd8f0,#7cc8ea)"></div>
    <div class="sale-tag">SALE</div><div class="sale-box"><span>25%</span><span>Sale</span></div>
  </div>
  <div class="abs card" style="left:851px">
    <div class="card-img" role="img" aria-label="Pink sleeping bag" style="background:linear-gradient(#f4bfdc,#eea9cf)"></div>
  </div>

  <div class="abs p-title" style="left:130px">Baby Sleeping Bag - 1</div>
  <div class="abs p-title" style="left:370px">Baby Sleeping Bag - 2</div>
  <div class="abs p-title" style="left:609px">Baby Sleeping Bag - 3</div>
  <div class="abs p-title" style="left:852px">Baby Sleeping Bag -4</div>
  <p class="abs p-desc" style="left:130px">Let your baby sleep with utmost comfort!!</p>
  <p class="abs p-desc" style="left:370px">Let your baby sleep with utmost comfort!!</p>
  <p class="abs p-desc" style="left:609px">Let your baby sleep with utmost comfort!!</p>
  <p class="abs p-desc" style="left:852px">Let your baby sleep with utmost comfort!!</p>
  <div class="abs p-price" style="left:130px">$ 25</div>
  <div class="abs p-price" style="left:370px">$ 25</div>
  <div class="abs p-price" style="left:609px">$ 25</div>
  <div class="abs p-price" style="left:852px">$ 25</div>
  <div class="abs btn btn-cart" style="left:130px">Add to cart</div>
  <div class="abs btn btn-info" style="left:246px">More Info</div>
  <div class="abs btn btn-cart" style="left:370px">Add to cart</div>
  <div class="abs btn btn-info" style="left:486px">More Info</div>
  <div class="abs btn btn-cart" style="left:609px">Add to cart</div>
  <div class="abs btn btn-info" style="left:725px">More Info</div>
  <div class="abs btn btn-cart" style="left:852px">Add to cart</div>
  <div class="abs btn btn-info" style="left:968px">More Info</div>

  <h2 class="abs section-title script" style="left:145px;top:902px">Follow us on chatterly</h2>
  <h2 class="abs section-title script" style="left:465px;top:902px">Newsletter</h2>
  <h2 class="abs section-title script" style="left:790px;top:902px">Special Offers</h2>

  <div class="abs box" style="left:147px">
    <div class="social-brand">Snugbag</div>
    <div class="like"><b>Like</b>327,796</div>
    <div class="fans">
      <div class="fan"><div role="img" aria-label="Fan photo"></div>Arlen</div>
      <div class="fan"><div role="img" aria-label="Fan photo"></div>Pemo</div>
      <div class="fan"><div role="img" aria-label="Fan photo"></div>Ravik</div>
      <div class="fan"><div role="img" aria-label="Fan photo"></div>Lio</div>
      <div class="fan"><div role="img" aria-label="Fan photo"></div>Nadi</div>
      <div class="fan"><div role="img" aria-label="Fan photo"></div>Oden</div>
      <div class="fan"><div role="img" aria-label="Fan photo"></div>Kavella</div>
      <div class="fan"><div role="img" aria-label="Fan photo"></div>Tovin</div>
      <div class="fan"><div role="img" aria-label="Fan photo"></div>Mira</div>
      <div class="fan"><div role="img" aria-label="Fan photo"></div>Sorelan</div>
    </div>
    <div class="plugin"><i></i>Chatterly social plugin</div>
  </div>

  <div class="abs box" style="left:465px">
    <div class="nl-head">
      <svg width="28" height="19" viewBox="0 0 28 19"><rect x="1" y="1" width="26" height="17" fill="none" stroke="#bbb" stroke-width="2"/><path d="M1 1l13 10L27 1" fill="none" stroke="#bbb" stroke-width="2"/></svg>
      SIGN UP NEWSLETTER
    </div>
    <p class="nl-text">Lorem Ipsum is simply dummy text of the printing and typesetting industry.</p>
    <div class="nl-input">Enter the E-mail Address</div>
    <div class="nl-submit">SUBMIT</div>
  </div>

  <div class="abs offer" role="img" aria-label="Photo of a happy baby playing with toys on a rug">
    <div class="offer-circle"><div class="a">25% OFF</div><div class="b">ON SLEEPING</div><div class="c">BAGS</div></div>
  </div>

  <footer class="abs footer">
    <div class="foot-links">Home<span>|</span>About Us<span>|</span>Sleeping Bags<span>|</span>Gifts<span>|</span>Sale<span>|</span>Contact Us</div>
    <div class="copy">© 2013 Snugbags ,All&nbsp; rights reserved</div>
    <div class="socials"><i></i><i></i><i></i><i></i></div>
  </footer>
</div>
</body>
</html>
```